Need a creative cover photo for social media profiles

We are rebranding and would like to promote the new look on our cover image for our social platforms (LinkedIn, Facebook, Twitter). It should feel similar in brand as the attached collateral. We want this to make a statement as our new logo and feel are completely different from where we currently are. I am sending along examples of other collateral we have created.
Target Market(s)
IT, accounting professionals and companies looking to hire those professionals.
Industry/Entity Type
Staffing
Requirements
Must have
- Logo
Our corporate font is Nexa Bold for headlines and Ebrima for content.
CMYK combinations for our corporate colors
C 2. M 66, Y 87, K 0
C 84, M 69, Y 47, K 39

```html
<!DOCTYPE html>
<html lang="en">
<head>
<meta charset="UTF-8">
<title>Norvale Group – Social Cover Variants</title>
<link rel="stylesheet" href="https://fonts.googleapis.com/css2?family=Montserrat:wght@700&family=Hind:wght@400&display=swap">
<style>
  :root {
    --brand-orange: #ec7636;
    --brand-navy: #0654a6;
    --peach: #e4a482;
    --sky: #8caccd;
    --white: #ffffff;
    --page: #ffffff;
  }
  * { margin: 0; padding: 0; box-sizing: border-box; }
  html, body {
    width: 1200px;
    height: 964px;
    overflow: hidden;
    background: var(--page);
  }
  .canvas {
    position: relative;
    width: 1200px;
    height: 964px;
  }
  .cover {
    position: absolute;
    left: 37px;
    width: 1122px;
    height: 415px;
    overflow: hidden;
    box-shadow: 0 0 40px rgba(0, 0, 0, 0.12);
  }
  .cover--blue { top: 48px; }
  .cover--orange { top: 497px; }

  .cover__photo {
    position: absolute;
    inset: 0;
  }
  .cover--blue .cover__photo {
    background: linear-gradient(180deg, var(--peach) 0%, #b88e8a 35%, #4e6d9e 62%, var(--brand-navy) 100%);
  }
  .cover--orange .cover__photo {
    background: linear-gradient(180deg, var(--sky) 0%, #a49aa6 35%, #c98266 62%, var(--brand-orange) 100%);
  }

  .brand-mark {
    position: absolute;
    left: 172px;
    top: 147px;
    width: 142px;
    height: 142px;
    border-radius: 50%;
    background: var(--brand-orange);
    box-shadow: 0 4px 14px rgba(0, 0, 0, 0.18);
  }
  .brand-name {
    position: absolute;
    left: 337px;
    top: 186px;
    font-family: "Montserrat", sans-serif;
    font-weight: 700;
    font-size: 62px;
    line-height: 62px;
    letter-spacing: 6px;
    color: var(--white);
    white-space: nowrap;
  }
  .cover__copy {
    position: absolute;
    left: 191px;
    top: 323px;
    width: 720px;
    font-family: "Hind", sans-serif;
    font-weight: 400;
    font-size: 16.5px;
    line-height: 25px;
    color: var(--white);
  }
</style>
</head>
<body>
<main class="canvas">
  <section class="cover cover--blue">
    <div class="cover__photo" role="img" aria-label="Photo of a smiling team of professionals shaking hands in a bright office, tinted peach to blue"></div>
    <div class="brand-mark"></div>
    <h1 class="brand-name">NORVALE GROUP</h1>
    <p class="cover__copy">Lorem ipsum dolor sit amet, consectetur adipiscing elit, sed do eiusmod tempor incididunt<br>ut labore et dolore magna aliqua. Quis ipsum suspendisse ultrices gravida. Risus commodo</p>
  </section>

  <section class="cover cover--orange">
    <div class="cover__photo" role="img" aria-label="Photo of a smiling team of professionals shaking hands in a bright office, tinted blue to orange"></div>
    <div class="brand-mark"></div>
    <h1 class="brand-name">NORVALE GROUP</h1>
    <p class="cover__copy">Lorem ipsum dolor sit amet, consectetur adipiscing elit, sed do eiusmod tempor incididunt<br>ut labore et dolore magna aliqua. Quis ipsum suspendisse ultrices gravida. Risus commodo</p>
  </section>
</main>
</body>
</html>
```